Visitenkarten-Design für klassischen Bauernhof
Vielen Dank für die tolle Zusammenarbeit Henrike. Die Visitenkarten sind genau so wie wir sie uns vorgestellt haben. Jederzeit gerne wieder :) LG Ulrike
Liebe Designer,
wir sind ein klassicher Bauernhof mit Ziegen und Direktvermarktung (SB-Hofladen).
Informationen über die Visitenkarten sind unter 'Vorgaben' aufgelistet.
Vielen Dank!
NACHTRAG - VIELEN HERZLICHEN DANK AN ALLE GRAFIKER FÜR DIE UNZÄHLIGEN WIRKLICH RESTLOS TOLLEN DESIGNS!!
DAS WAR KEINE LEICHTE ENTSCHEIDUNG...
Aufgabenstellung
Folgende Angaben sollten auf der Visitenkarte enthalten sein:
Ziegenhof Brunnrieth (Logo)
SB Hofladen täglich geöffnet
Hofkäserei
Die Visitenkarten kann gerne auch beidseitig bedruckt werden.
Eine Zeile um ggf. eine Mobilfunknummer eintragen zu können wäre praktisch aber nicht dringend notwendig (ebenso ein Ziegenbild)

```html
<!DOCTYPE html>
<html lang="de">
<head>
<meta charset="utf-8">
<title>Ziegenhof Brunnrieth – Visitenkarten</title>
<link rel="stylesheet" href="https://fonts.googleapis.com/css2?family=Montserrat:wght@300;500;600&family=Caveat:wght@600&display=swap">
<style>
  :root {
    --cream: #e4e5dd;
    --white: #ffffff;
    --brown: #653826;
    --green: #009a3e;
    --yellow: #f8bb55;
    --charcoal: #424345;
    --link-blue: #4a8fb5;
    --text-brown: #5b3a2c;
    --stage: #e4e4e4;
  }
  * { margin: 0; padding: 0; box-sizing: border-box; }
  html, body { width: 848px; height: 1200px; overflow: hidden; background: var(--white); }
  body { position: relative; font-family: "Montserrat", sans-serif; }

  .card {
    position: absolute;
    width: 100em;
    height: 64.4em;
    font-size: 3.43px;
    overflow: hidden;
    box-shadow: 0.6em 0.8em 1.2em rgba(0,0,0,0.25);
    --card-bg: var(--cream);
    --band: var(--brown);
    --footer-text: var(--white);
    --badge-top: var(--green);
    background: var(--card-bg);
  }
  .card--white { --card-bg: var(--white); --band: var(--charcoal); --footer-text: var(--link-blue); border: 1px solid #888; }
  .card--green { --band: var(--green); --badge-top: var(--brown); }
  .card--large { font-size: 4.6px; box-shadow: 0.4em 0.6em 1.6em rgba(0,0,0,0.28); }

  .card__band { position: absolute; inset: 0; width: 100%; height: 100%; }
  .card__band polygon { fill: var(--band); }

  .logo { position: absolute; left: 4%; top: 6%; width: 35em; text-align: center; }
  .logo__emblem {
    display: block; width: 23em; height: 23em; margin: 0 auto;
    border-radius: 50%;
    background: radial-gradient(circle at 50% 40%, #7a5140 0%, #5a3324 45%, #3f8f3a 80%, #1f8a3c 100%);
    border: 0.5em solid var(--green);
  }
  .logo__name {
    margin-top: 2.2em;
    color: var(--text-brown);
    font-weight: 600;
    font-size: 4.2em;
    line-height: 1.05;
  }

  .contact { position: absolute; left: 43.5%; top: 8.4%; color: var(--text-brown); white-space: nowrap; }
  .contact__title { font-size: 3.4em; font-weight: 500; line-height: 1; margin-bottom: 0.6em; }
  .contact__title span { color: var(--green); }
  .contact__lines { list-style: none; font-size: 3.05em; font-weight: 300; line-height: 1.42; }

  .badge {
    position: absolute; left: 71%; top: 48%;
    width: 23.5em; height: 23.5em; border-radius: 50%; overflow: hidden;
    background: linear-gradient(to bottom, var(--badge-top) 0 57%, var(--white) 57% 59%, var(--yellow) 59% 100%);
    border: 0.4em solid var(--white);
    font-family: "Caveat", cursive; color: var(--white); text-align: center;
    white-space: nowrap;
  }
  .badge__main { position: absolute; top: 17%; left: 0; right: 0; font-size: 3.5em; line-height: 1.05; transform: rotate(-5deg); }
  .badge__sub { position: absolute; top: 67%; left: 0; right: 0; font-size: 3.4em; line-height: 1; transform: rotate(-5deg); }

  .footer {
    position: absolute; left: 5.6%; top: 86.2%;
    display: flex; align-items: center; white-space: nowrap;
    color: var(--footer-text); font-weight: 500; font-size: 2.5em;
  }
  .footer__sep { margin: 0 0.8em; }
  .footer__social {
    position: absolute; right: 2.5%; top: 86.4%;
    color: var(--footer-text); font-size: 2.3em; font-weight: 600; white-space: nowrap;
  }

  .stage { position: absolute; left: 68px; top: 614px; width: 706px; height: 529px; background: var(--stage); }
</style>
</head>
<body>

<div class="stage"></div>

<article class="card card--cream" style="left:68px; top:42px;">
  <svg class="card__band" viewBox="0 0 100 64.4" preserveAspectRatio="none" aria-hidden="true"><polygon points="0,51 100,43.4 100,64.4 0,64.4"/></svg>
  <div class="logo">
    <span class="logo__emblem" role="img" aria-label="Ziegen-Illustration auf Wiese im grünen Kreis"></span>
    <p class="logo__name">Ziegenhof<br>Brunnrieth</p>
  </div>
  <div class="contact">
    <h2 class="contact__title">Ziegenhof <span>Brunnrieth</span></h2>
    <ul class="contact__lines">
      <li>Familie Korber</li><li>Brunnriethsiedlung 1</li><li>77889 Lindenau</li>
      <li>(Post: 77856 Talbach-Erlenhurst)</li><li>T. 07852-419</li><li>M. 0171-5550142</li><li>F. 07852-638</li>
    </ul>
  </div>
  <div class="badge"><p class="badge__main">SB Hofladen<br>täglich geöffnet</p><p class="badge__sub">Hofkäserei</p></div>
  <div class="footer"><span>ziegenhof-brunnrieth.de</span><span class="footer__sep">•</span><span>info@ziegenhof-brunnrieth.de</span></div>
  <span class="footer__social">Hofnetz</span>
</article>

<article class="card card--green" style="left:438px; top:211px;">
  <svg class="card__band" viewBox="0 0 100 64.4" preserveAspectRatio="none" aria-hidden="true"><polygon points="0,51 100,43.4 100,64.4 0,64.4"/></svg>
  <div class="logo">
    <span class="logo__emblem" role="img" aria-label="Ziegen-Illustration auf Wiese im grünen Kreis"></span>
    <p class="logo__name">Ziegenhof<br>Brunnrieth</p>
  </div>
  <div class="contact">
    <h2 class="contact__title">Ziegenhof <span>Brunnrieth</span></h2>
    <ul class="contact__lines">
      <li>Familie Korber</li><li>Brunnriethsiedlung 1</li><li>77889 Lindenau</li>
      <li>(Post: 77856 Talbach-Erlenhurst)</li><li>T. 07852-419</li><li>M. 0171-5550142</li><li>F. 07852-638</li>
    </ul>
  </div>
  <div class="badge"><p class="badge__main">SB Hofladen<br>täglich geöffnet</p><p class="badge__sub">Hofkäserei</p></div>
  <div class="footer"><span>ziegenhof-brunnrieth.de</span><span class="footer__sep">•</span><span>info@ziegenhof-brunnrieth.de</span></div>
  <span class="footer__social">Hofnetz</span>
</article>

<article class="card card--white" style="left:68px; top:350px;">
  <svg class="card__band" viewBox="0 0 100 64.4" preserveAspectRatio="none" aria-hidden="true"><polygon points="0,51 100,43.4 100,64.4 0,64.4"/></svg>
  <div class="logo">
    <span class="logo__emblem" role="img" aria-label="Ziegen-Illustration auf Wiese im grünen Kreis"></span>
    <p class="logo__name">Ziegenhof<br>Brunnrieth</p>
  </div>
  <div class="contact">
    <h2 class="contact__title">Ziegenhof <span>Brunnrieth</span></h2>
    <ul class="contact__lines">
      <li>Familie Korber</li><li>Brunnriethsiedlung 1</li><li>77889 Lindenau</li>
      <li>(Post: 77856 Talbach-Erlenhurst)</li><li>T. 07852-419</li><li>M. 0171-5550142</li><li>F. 07852-638</li>
    </ul>
  </div>
  <div class="badge"><p class="badge__main">SB Hofladen<br>täglich geöffnet</p><p class="badge__sub">Hofkäserei</p></div>
  <div class="footer"><span>ziegenhof-brunnrieth.de</span><span class="footer__sep">•</span><span>info@ziegenhof-brunnrieth.de</span></div>
  <span class="footer__social">Hofnetz</span>
</article>

<article class="card card--cream card--large" style="left:191px; top:730px;">
  <svg class="card__band" viewBox="0 0 100 64.4" preserveAspectRatio="none" aria-hidden="true"><polygon points="0,51 100,43.4 100,64.4 0,64.4"/></svg>
  <div class="logo">
    <span class="logo__emblem" role="img" aria-label="Ziegen-Illustration auf Wiese im grünen Kreis"></span>
    <p class="logo__name">Ziegenhof<br>Brunnrieth</p>
  </div>
  <div class="contact">
    <h2 class="contact__title">Ziegenhof <span>Brunnrieth</span></h2>
    <ul class="contact__lines">
      <li>Familie Korber</li><li>Brunnriethsiedlung 1</li><li>77889 Lindenau</li>
      <li>(Post: 77856 Talbach-Erlenhurst)</li><li>T. 07852-419</li><li>M. 0171-5550142</li><li>F. 07852-638</li>
    </ul>
  </div>
  <div class="badge"><p class="badge__main">SB Hofladen<br>täglich geöffnet</p><p class="badge__sub">Hofkäserei</p></div>
  <div class="footer"><span>ziegenhof-brunnrieth.de</span><span class="footer__sep">•</span><span>info@ziegenhof-brunnrieth.de</span></div>
  <span class="footer__social">Hofnetz</span>
</article>

</body>
</html>
```